New Flyer Design Project

We need a flyer for our upcoming Rising Builders Forum.

5th Annual Rising Builders Forum
by the Council for Stewardship of Built Ventures (C-SBuV)
Theme: Step Forward
Date: January 24, 2020
Location: Bluestone Lodge Hotel and Conference Center, San Marcos, TX
#StepForward

This is event is put together by C-SBuV's Rising Builders Ring of Merit. I have a logo for the Ring of Merit, but not something that indicates it's the Rising Builders Ring.

More about the Forum (please don't include on the flyer): This Forum provides a venue to openly discuss issues affecting women in our industry and ideas and strategies to address those issues.

Architecture, Construction and Engineering are all struggling with a tremendous shortage of skilled talent. It is more important than ever for organizations to be able to attract, support and retain a talented workforce and to encourage more women to pursue and build vibrant careers in architecture, engineering and construction. Unfortunately, their attrition rate also remains high in these industries. Developing and retaining a skilled workforce includes identifying and addressing the specific needs of women in our industry. Man or Woman; Male or Female Brain, C-SBuV’s Rising Builders Forum will give you and your team the tools you need to excel as an Employer of Choice and a roadmap for individual continued career planning and success .

This unique Forum provides a venue to engage everyone from executives to those just beginning their careers with active, hands-on sessions and vibrant networking with the best and brightest in the A/E/C industry. In our usual C-SBuV Forum style, Keynotes become table participants and table participants become presenters, encouraging participants to assimilate what they are learning. Join local, state and national leaders and subject matter experts as we candidly explore and address the issues affecting women in our industry .

```html
<!DOCTYPE html>
<html lang="en">
<head>
<meta charset="utf-8">
<title>Rising Builders Forum Flyer</title>
<link href="https://fonts.googleapis.com/css2?family=Montserrat:wght@600;800&family=Arimo:wght@400&display=swap" rel="stylesheet">
<style>
  :root {
    --brand-blue: #1d4093;
    --brand-green: #8ab43c;
    --header-tint: #fdf7f9;
    --ink: #3a3a3a;
    --logo-grey: #555a60;
    --backdrop: #e4e4e4;
    --white: #ffffff;
  }
  html, body {
    margin: 0;
    width: 1200px;
    height: 2504px;
    overflow: hidden;
    background: var(--backdrop);
  }
  .flyer {
    position: absolute;
    left: 50px;
    top: 473px;
    width: 838px;
    height: 1186px;
    transform: scale(1.3126);
    transform-origin: 0 0;
    overflow: hidden;
    background: var(--white);
    box-shadow: 0 6px 18px rgba(0,0,0,0.25);
  }
  .masthead {
    position: absolute;
    left: 0; top: 0;
    width: 838px; height: 162px;
    background: var(--header-tint);
    display: flex;
    align-items: center;
    justify-content: center;
    gap: 22px;
  }
  .masthead-mark {
    width: 92px; height: 92px;
    border-radius: 50%;
    background: var(--brand-blue);
  }
  .masthead-name {
    font-family: "Montserrat", sans-serif;
    font-weight: 600;
    font-size: 58px;
    color: var(--logo-grey);
    letter-spacing: 1px;
  }
  .skyline-photo {
    position: absolute;
    left: 0; top: 162px;
    width: 838px; height: 380px;
    background: linear-gradient(180deg, #3a4a6e 0%, #c98a6a 28%, #4a5470 45%, #1e2a40 70%, #2a3550 100%);
  }
  .shapes {
    position: absolute;
    left: 0; top: 0;
    width: 838px; height: 1186px;
  }
  .event-title {
    position: absolute;
    left: 10px; top: 572px;
    width: 375px;
    margin: 0;
    text-align: center;
    font-family: "Montserrat", sans-serif;
    font-weight: 800;
    font-size: 38px;
    line-height: 44px;
    color: var(--white);
  }
  .event-host {
    position: absolute;
    left: 20px; top: 756px;
    width: 355px;
    margin: 0;
    text-align: center;
    font-family: "Arimo", sans-serif;
    font-size: 19px;
    line-height: 25px;
    color: var(--white);
  }
  .ring-badge {
    position: absolute;
    left: 0; top: 872px;
    width: 395px;
    display: flex;
    align-items: center;
    justify-content: center;
    gap: 14px;
  }
  .ring-badge-mark {
    width: 54px; height: 54px;
    border-radius: 50%;
    border: 8px solid var(--white);
    box-sizing: border-box;
  }
  .ring-badge-name {
    font-family: "Arimo", sans-serif;
    font-size: 28px;
    color: var(--white);
  }
  .theme-block {
    position: absolute;
    left: 410px; top: 512px;
    width: 420px;
    text-align: center;
  }
  .theme-heading {
    margin: 0;
    font-family: "Montserrat", sans-serif;
    font-weight: 800;
    font-size: 38px;
    line-height: 46px;
    color: var(--brand-blue);
  }
  .theme-name {
    margin: 120px 0 0;
    font-family: "Montserrat", sans-serif;
    font-weight: 800;
    font-size: 50px;
    line-height: 60px;
    color: var(--brand-blue);
  }
  .theme-hashtag {
    margin: 18px 0 0;
    font-family: "Montserrat", sans-serif;
    font-weight: 600;
    font-size: 30px;
    line-height: 36px;
    color: var(--brand-green);
  }
  .event-date {
    position: absolute;
    left: 410px; top: 990px;
    width: 420px;
    margin: 0;
    text-align: center;
    font-family: "Montserrat", sans-serif;
    font-weight: 800;
    font-size: 36px;
    color: var(--brand-green);
  }
  .contact-bar {
    position: absolute;
    left: 0; top: 1128px;
    width: 838px; height: 52px;
    font-family: "Arimo", sans-serif;
    font-size: 16.5px;
    line-height: 20px;
    color: var(--white);
  }
  .contact-item {
    position: absolute;
    display: flex;
    align-items: center;
    gap: 10px;
    top: 0; height: 52px;
  }
  .contact-venue { left: 26px; }
  .contact-phone { left: 360px; }
  .contact-web { left: 540px; }
  .contact-item svg { flex: none; }
</style>
</head>
<body>
  <main class="flyer">
    <header class="masthead">
      <span class="masthead-mark"></span>
      <span class="masthead-name">C-SBuV</span>
    </header>

    <div class="skyline-photo" role="img" aria-label="Evening city skyline above a river at sunset"></div>

    <svg class="shapes" viewBox="0 0 838 1186" aria-hidden="true">
      <path d="M0,470 C90,500 200,512 320,496 C500,470 680,420 838,420 L838,1080 C700,1120 560,1100 420,1060 C300,1020 150,1000 0,1060 Z" fill="var(--white)"/>
      <path d="M0,488 C100,512 250,512 400,486 C560,458 700,430 838,436 L838,448 C700,446 560,472 400,502 C250,530 100,530 0,514 Z" fill="var(--brand-green)"/>
      <path d="M0,512 C100,530 250,526 400,500 L400,1040 C280,1005 130,1010 0,1060 Z" fill="var(--brand-blue)"/>
      <path d="M0,1080 C150,1020 300,1022 450,1055 C600,1088 720,1092 838,1066 L838,1082 C720,1112 600,1112 450,1084 C300,1058 150,1060 0,1112 Z" fill="var(--brand-green)"/>
      <path d="M0,1112 C150,1060 300,1058 450,1084 C600,1112 720,1112 838,1082 L838,1186 L0,1186 Z" fill="var(--brand-blue)"/>
    </svg>

    <h1 class="event-title">5TH ANNUAL<br>RISING<br>BUILDERS<br>FORUM</h1>
    <p class="event-host">by the Council for Stewardship of Built Ventures (C-SBuV)</p>

    <div class="ring-badge">
      <span class="ring-badge-mark"></span>
      <span class="ring-badge-name">Rings of Merit</span>
    </div>

    <section class="theme-block">
      <h2 class="theme-heading">OUR THEME:</h2>
      <p class="theme-name">Step Forward</p>
      <p class="theme-hashtag">#StepForward</p>
    </section>

    <p class="event-date">JANUARY 24, 2020</p>

    <footer class="contact-bar">
      <div class="contact-item contact-venue">
        <svg width="20" height="28" viewBox="0 0 20 28"><path d="M10,0 C4.5,0 0,4.4 0,9.8 C0,17 10,28 10,28 C10,28 20,17 20,9.8 C20,4.4 15.5,0 10,0 Z M10,14 C7.6,14 5.8,12.1 5.8,9.8 C5.8,7.5 7.6,5.6 10,5.6 C12.4,5.6 14.2,7.5 14.2,9.8 C14.2,12.1 12.4,14 10,14 Z" fill="var(--brand-green)"/></svg>
        <span>Bluestone Lodge Hotel and<br>Conference Center, San Marcos, TX</span>
      </div>
      <div class="contact-item contact-phone">
        <svg width="26" height="26" viewBox="0 0 26 26"><circle cx="13" cy="13" r="11.5" fill="none" stroke="var(--brand-green)" stroke-width="2"/><path d="M8.5,7 L10.8,7 L11.8,10.2 L10.3,11.4 C11,13 12.6,14.7 14.4,15.6 L15.7,14.1 L18.8,15.2 L18.8,17.4 C18.8,18.2 18,18.8 17.2,18.7 C12,18 7.8,13.8 7.2,8.6 C7.1,7.8 7.7,7 8.5,7 Z" fill="var(--brand-green)"/></svg>
        <span>(512) 555-0148</span>
      </div>
      <div class="contact-item contact-web">
        <svg width="26" height="26" viewBox="0 0 26 26" fill="none" stroke="var(--brand-green)" stroke-width="1.8"><circle cx="13" cy="13" r="11"/><ellipse cx="13" cy="13" rx="5" ry="11"/><line x1="2" y1="13" x2="24" y2="13"/><path d="M4,7 H22 M4,19 H22"/></svg>
        <span>www.c-sbuv-forum.org</span>
      </div>
    </footer>
  </main>
</body>
</html>
```